Business Card and Stationary
Small management consulting firm
Professional
Dwight Parmelee
President
5142 Heron Loop
Dunmore Crossing, VA 22817
dwight.parmelee@lw-advis.com
http://www.lw-advis.com
Our audience will be industry members of the defense consulting world as well as the US Government so we will need something memorable, but nothing too over the top.
Our Logo,
The slogan: "Real Strategy, Meaningful Change"
Our website: www.lw-advis.com
Here is the second design with our logo on the side

```html
<!DOCTYPE html>
<html lang="en">
<head>
<meta charset="utf-8">
<title>Lodgewood Advisory Stationery</title>
<link href="https://fonts.googleapis.com/css2?family=Cinzel:wght@600&family=Open+Sans:wght@400;600&display=swap" rel="stylesheet">
<style>
  :root {
    --board: #2e2f31;
    --board-light: #3a3b3e;
    --paper: #ffffff;
    --navy: #1d4f96;
    --blue: #2f6fc4;
    --sky: #7fb1e6;
    --red: #c3242b;
    --ink: #2a3550;
    --muted: #8a8f99;
    --caption: #9a9ca1;
  }
  * { margin: 0; padding: 0; box-sizing: border-box; }
  html, body { width: 1200px; height: 310px; overflow: hidden; }
  body {
    background: radial-gradient(ellipse at 30% 40%, var(--board-light), var(--board) 70%);
    font-family: "Open Sans", Arial, sans-serif;
    position: relative;
  }
  .item { position: absolute; }
  .paper { background: var(--paper); box-shadow: 0 2px 6px rgba(0,0,0,.5); }
  .caption {
    position: absolute; left: 0; right: 0; bottom: -12px;
    font-size: 6px; color: var(--caption); text-align: center;
  }
  .brand { display: flex; align-items: center; gap: 5px; }
  .brand-dot { border-radius: 50%; background: var(--navy); flex: none; }
  .brand-name {
    font-family: "Cinzel", Georgia, serif; font-weight: 600;
    color: var(--navy); line-height: 1.1; letter-spacing: .3px;
  }

  /* board title */
  .board-title { left: 14px; top: 12px; width: 120px; }
  .board-title .brand-dot { width: 22px; height: 22px; background: #fff; }
  .board-title .brand-name { color: #fff; font-size: 11px; }
  .board-title .subtitle { color: var(--caption); font-size: 6px; margin-top: 10px; }

  /* business cards */
  .card { width: 104px; height: 58px; padding: 7px; }
  .card-front { left: 14px; top: 90px; }
  .card-front .brand-dot { width: 10px; height: 10px; }
  .card-front .brand-name { font-size: 6px; }
  .card-front .details { position: absolute; right: 7px; top: 22px; font-size: 4px; color: var(--ink); line-height: 1.45; text-align: right; }
  .card-front .details strong { font-size: 5px; font-weight: 600; }
  .card-white { left: 14px; top: 212px; }
  .card-white .brand { position: absolute; left: 14px; top: 20px; }
  .card-white .brand-dot { width: 14px; height: 14px; background: var(--red); }
  .card-white .brand-name { font-size: 6px; }
  .card-blue { left: 124px; top: 212px; background: linear-gradient(135deg, var(--blue), var(--navy)); }
  .card-blue .brand { position: absolute; left: 22px; top: 16px; flex-direction: column; gap: 3px; }
  .card-blue .brand-dot { width: 16px; height: 16px; background: #fff; }
  .card-blue .brand-name { font-size: 5px; color: #fff; }

  /* letterheads */
  .letterhead { top: 12px; width: 200px; height: 272px; overflow: hidden; }
  .letterhead-a { left: 266px; }
  .letterhead-b { left: 490px; }
  .letterhead .band {
    position: absolute; left: 0; top: 0; bottom: 0; width: 20px;
    background: linear-gradient(180deg, var(--navy), var(--blue) 55%, var(--sky));
  }
  .letterhead .brand { position: absolute; left: 26px; top: 16px; }
  .letterhead .brand-dot { width: 12px; height: 12px; }
  .letterhead .brand-name { font-size: 6.5px; }
  .letterhead .contact { position: absolute; right: 10px; top: 16px; font-size: 3.5px; color: var(--muted); line-height: 1.5; text-align: right; }
  .letterhead .rule { position: absolute; left: 26px; right: 10px; top: 36px; height: 1px; background: var(--sky); }
  .letterhead .footer { position: absolute; left: 26px; right: 10px; bottom: 10px; font-size: 3.5px; color: var(--muted); text-align: center; }
  .letterhead .tagline { position: absolute; left: 26px; right: 10px; bottom: 20px; font-size: 4px; color: var(--navy); text-align: center; font-style: normal; }

  /* notecards */
  .note { left: 722px; width: 108px; height: 50px; }
  .note-a { top: 108px; }
  .note-b { top: 218px; }
  .note .band { position: absolute; left: 0; top: 0; bottom: 0; width: 10px; background: linear-gradient(180deg, var(--navy), var(--sky)); }
  .note .brand { position: absolute; left: 16px; top: 8px; }
  .note .brand-dot { width: 9px; height: 9px; }
  .note .brand-name { font-size: 5px; }
  .note .url { position: absolute; right: 6px; bottom: 5px; font-size: 3.5px; color: var(--muted); }

  /* envelopes */
  .envelope { left: 842px; width: 346px; height: 56px; }
  .envelope svg { position: absolute; inset: 0; }
  .env-red { top: 112px; }
  .env-blue { top: 176px; }
  .env-white { top: 240px; height: 48px; }
  .envelope .brand { position: absolute; left: 10px; top: 24px; }
  .envelope .brand-dot { width: 10px; height: 10px; }
  .envelope .brand-name { font-size: 5px; }
  .env-blue .brand { top: 8px; }
</style>
</head>
<body>

  <section class="item board-title">
    <div class="brand">
      <span class="brand-dot"></span>
      <span class="brand-name">Lodgewood Advisory, LLC</span>
    </div>
    <p class="subtitle">Stationery Concept</p>
  </section>

  <article class="item card card-front paper">
    <div class="brand"><span class="brand-dot"></span><span class="brand-name">Lodgewood Advisory, LLC</span></div>
    <div class="details">
      <strong>Dwight Parmelee</strong><br>President<br>
      5142 Heron Loop<br>Dunmore Crossing, VA 22817<br>
      dwight.parmelee@lw-advis.com<br>http://www.lw-advis.com
    </div>
    <span class="caption">Card Front</span>
  </article>

  <article class="item card card-white paper">
    <div class="brand"><span class="brand-dot"></span><span class="brand-name">Lodgewood Advisory, LLC</span></div>
  </article>

  <article class="item card card-blue paper">
    <div class="brand"><span class="brand-dot"></span><span class="brand-name">Lodgewood Advisory, LLC</span></div>
    <span class="caption">Card Back</span>
  </article>

  <article class="item letterhead letterhead-a paper">
    <div class="band"></div>
    <div class="brand"><span class="brand-dot"></span><span class="brand-name">Lodgewood Advisory, LLC</span></div>
    <div class="contact">5142 Heron Loop<br>Dunmore Crossing, VA 22817<br>www.lw-advis.com</div>
    <div class="rule"></div>
    <p class="tagline">Real Strategy, Meaningful Change</p>
    <p class="footer">dwight.parmelee@lw-advis.com · http://www.lw-advis.com</p>
  </article>
  <span class="item caption" style="left:266px;width:200px;top:286px;bottom:auto">Letterhead</span>

  <article class="item letterhead letterhead-b paper">
    <div class="band"></div>
    <div class="brand"><span class="brand-dot"></span><span class="brand-name">Lodgewood Advisory, LLC</span></div>
    <div class="rule"></div>
    <p class="tagline">Real Strategy, Meaningful Change</p>
    <p class="footer">5142 Heron Loop · Dunmore Crossing, VA 22817 · www.lw-advis.com</p>
  </article>
  <span class="item caption" style="left:490px;width:200px;top:286px;bottom:auto">Letterhead</span>

  <article class="item note note-a paper">
    <div class="band"></div>
    <div class="brand"><span class="brand-dot"></span><span class="brand-name">Lodgewood Advisory, LLC</span></div>
    <span class="url">www.lw-advis.com</span>
    <span class="caption">Notecard</span>
  </article>

  <article class="item note note-b paper">
    <div class="band"></div>
    <div class="brand"><span class="brand-dot"></span><span class="brand-name">Lodgewood Advisory, LLC</span></div>
    <span class="url">www.lw-advis.com</span>
    <span class="caption">Notecard</span>
  </article>

  <article class="item envelope env-red paper">
    <svg viewBox="0 0 346 56" preserveAspectRatio="none">
      <path d="M0 0 H346 L173 22 Z" fill="var(--red)"/>
    </svg>
    <div class="brand"><span class="brand-dot"></span><span class="brand-name">Lodgewood Advisory, LLC</span></div>
  </article>

  <article class="item envelope env-blue paper">
    <svg viewBox="0 0 346 56" preserveAspectRatio="none">
      <path d="M0 56 V30 Q173 12 346 30 V56 Z" fill="var(--blue)"/>
    </svg>
    <div class="brand"><span class="brand-dot"></span><span class="brand-name">Lodgewood Advisory, LLC</span></div>
  </article>

  <article class="item envelope env-white paper">
    <svg viewBox="0 0 346 48" preserveAspectRatio="none">
      <path d="M0 0 L173 30 L346 0" fill="none" stroke="#d6dbe3" stroke-width="1"/>
      <path d="M0 48 L150 24 M346 48 L196 24" fill="none" stroke="#e3e6eb" stroke-width="1"/>
    </svg>
  </article>

</body>
</html>
```